Bref créative
Stationary for telecom company
KLV Telecommunications
Professional
Dinh Quoc Bao
Director
47 Hoa Lu Street, Ward 5, Go Vap District, Ho Chi Minh City
bao.dinh@mrq.net.vn
www.klvtelecom.vn

```html
<!DOCTYPE html>
<html lang="en">
<head>
<meta charset="utf-8">
<title>KLV Telecommunications – Business Card</title>
<link rel="stylesheet" href="https://fonts.googleapis.com/css2?family=Open+Sans:wght@400;600;700;800&display=swap">
<style>
  :root {
    --page-bg: #e9e7e3;
    --brand-blue: #2f5f9b;
    --brand-blue-dark: #22497d;
    --brand-blue-light: #4677b3;
    --swoosh: #111418;
    --card-white: #ffffff;
    --text-light: #ffffff;
    --text-soft: #dfe8f4;
  }
  * { box-sizing: border-box; margin: 0; padding: 0; }
  html, body { width: 1200px; height: 914px; overflow: hidden; }
  body {
    background: var(--page-bg);
    font-family: "Open Sans", Arial, sans-serif;
    position: relative;
  }
  .business-card {
    position: absolute;
    left: 150px; top: 197px;
    width: 900px; height: 520px;
    background: var(--card-white);
    box-shadow: 0 14px 34px rgba(0,0,0,0.18);
    overflow: hidden;
  }
  .card-shapes { position: absolute; inset: 0; }
  .holder { position: absolute; left: 60px; top: 52px; color: var(--text-light); }
  .holder-name { font-size: 30px; font-weight: 700; letter-spacing: 0.2px; }
  .holder-title { font-size: 20px; font-weight: 400; margin-top: 4px; color: var(--text-soft); }
  .contact-list {
    position: absolute; left: 60px; top: 300px;
    list-style: none; color: var(--text-light);
    font-size: 15px; line-height: 1.3;
  }
  .contact-item { display: flex; align-items: flex-start; gap: 12px; margin-bottom: 9px; }
  .contact-icon { flex: none; width: 22px; height: 22px; }
  .contact-item span { padding-top: 1px; }
  .brand-name {
    position: absolute; left: 470px; top: 232px; width: 400px;
    text-align: center;
    font-size: 34px; font-weight: 800;
    color: var(--brand-blue-dark);
    letter-spacing: 0.3px;
  }
</style>
</head>
<body>
  <div class="business-card">
    <svg class="card-shapes" viewBox="0 0 900 520" width="900" height="520" aria-hidden="true">
      <defs>
        <linearGradient id="blueFill" x1="0" y1="0" x2="1" y2="1">
          <stop offset="0" stop-color="var(--brand-blue-light)"/>
          <stop offset="1" stop-color="var(--brand-blue-dark)"/>
        </linearGradient>
      </defs>
      <path class="swoosh-line" d="M528 0 C448 60 436 200 456 300 C476 400 436 480 372 520" fill="none" stroke="var(--swoosh)" stroke-width="6"/>
      <path class="blue-panel" d="M0 0 H512 C432 60 420 200 440 300 C460 400 420 480 356 520 H0 Z" fill="url(#blueFill)"/>
    </svg>

    <div class="holder">
      <div class="holder-name">Dinh Quoc Bao</div>
      <div class="holder-title">Director</div>
    </div>

    <ul class="contact-list">
      <li class="contact-item">
        <svg class="contact-icon" viewBox="0 0 22 22"><circle cx="11" cy="11" r="11" fill="#fff"/><path d="M11 5a4 4 0 0 0-4 4c0 3 4 8 4 8s4-5 4-8a4 4 0 0 0-4-4zm0 5.5a1.5 1.5 0 1 1 0-3 1.5 1.5 0 0 1 0 3z" fill="var(--brand-blue)"/></svg>
        <span>47 Hoa Lu Street, Ward 5, Go Vap District,<br>Ho Chi Minh City</span>
      </li>
      <li class="contact-item">
        <svg class="contact-icon" viewBox="0 0 22 22"><circle cx="11" cy="11" r="11" fill="#fff"/><path d="M7.5 5.5l2 0 1 3-1.3 1a6 6 0 0 0 3.3 3.3l1-1.3 3 1v2a1.5 1.5 0 0 1-1.5 1.5A9 9 0 0 1 6 7a1.5 1.5 0 0 1 1.5-1.5z" fill="var(--brand-blue)"/></svg>
        <span>(84) 8 38 452610</span>
      </li>
      <li class="contact-item">
        <svg class="contact-icon" viewBox="0 0 22 22"><circle cx="11" cy="11" r="11" fill="#fff"/><rect x="6" y="7" width="10" height="9" rx="1" fill="var(--brand-blue)"/><rect x="8" y="5" width="6" height="3" fill="var(--brand-blue)"/><rect x="8" y="10" width="6" height="2" fill="#fff"/></svg>
        <span>(84) 8 38 452733</span>
      </li>
      <li class="contact-item">
        <svg class="contact-icon" viewBox="0 0 22 22"><circle cx="11" cy="11" r="11" fill="#fff"/><rect x="5.5" y="7" width="11" height="8" rx="1" fill="var(--brand-blue)"/><path d="M5.5 7.5l5.5 4 5.5-4" fill="none" stroke="#fff" stroke-width="1.2"/></svg>
        <span>bao.dinh@mrq.net.vn</span>
      </li>
      <li class="contact-item">
        <svg class="contact-icon" viewBox="0 0 22 22"><circle cx="11" cy="11" r="11" fill="#fff"/><circle cx="11" cy="11" r="5.5" fill="none" stroke="var(--brand-blue)" stroke-width="1.4"/><path d="M5.5 11h11M11 5.5c-2.5 3-2.5 8 0 11M11 5.5c2.5 3 2.5 8 0 11" fill="none" stroke="var(--brand-blue)" stroke-width="1.2"/></svg>
        <span>www.klvtelecom.vn</span>
      </li>
    </ul>

    <div class="brand-name">KLV Telecommunications</div>
  </div>
</body>
</html>
```